Redesign Opal's RV Park & Lodge Website, Leeds, North Dakota

I need a totally re-designed website for my RV Park / Lodge. I want to not only provide information on my RV Park / Lodge, I want to provide my customers with information on the town and area attractions. I want to provide rate information. Ideally, I would like to have a button/page for each section: Welcome & Information, Area Attractions, Welcome to Leeds, Rates, Who's Opal?!, FAQ's and Where are we?. I don't know if this would be more expensive the more pages you have? If more pages is too expensive, then we can combine info on less pages. I want my logo included on the web page. I want Mockup Forge to take down my old website and use the same address to put up my newly designed website.

Target Market(s)

Full time RVers, People who camp, hunt fish, People who recreate on Devils Lake, People who are looking for meeting/conference space, people who are looking for party venue

Industry/Entity Type

Accommodation

Number of Pages Required

3 page

Requirements
Must have
• I want a cozy, welcoming type web site. No super dark colors. Bright and cheerful.
• Must be simple and organized.
• NOTE: I have a file of pictures of the interior of Opal's Lodge that must be included in website. Please request this file if you will be designing my project as the files are too large to upload through Mockup Forge.
Nice to have
• If you cannot open any of the files listed, please notify me.
Should not have
• No stark or super-formal designs.

```html
<!DOCTYPE html>
<html lang="en">
<head>
<meta charset="utf-8">
<title>Opal's RV Park &amp; Lodge — Leeds, ND</title>
<link href="https://fonts.googleapis.com/css2?family=Arvo:wght@400;700&family=Delius&family=Dancing+Script:wght@600&display=swap" rel="stylesheet">
<style>
:root{
  --maroon:#7a1a1c;
  --maroon-dark:#6b1618;
  --green:#5c8a0a;
  --green-band:#638f00;
  --gold:#f0c21b;
  --ink:#333;
  --muted:#999;
  --white:#fff;
}
*{margin:0;padding:0;box-sizing:border-box}
html,body{width:1200px;height:2200px;overflow:hidden;background:var(--white)}
body{position:relative;font-family:"Delius",cursive;color:var(--ink)}
.abs{position:absolute}
.nowrap{white-space:nowrap}
.site-header{left:0;top:0;width:1200px;height:120px;background:linear-gradient(180deg,#8b2224,#731a1c)}
.logo-box{left:70px;top:0;width:184px;height:213px;background:var(--white);border-radius:0 0 22px 22px;z-index:3;display:flex;flex-direction:column;align-items:center;justify-content:center;gap:12px;text-align:center}
.logo-mark{width:46px;height:46px;background:var(--maroon);border-radius:50%}
.logo-name{font-family:"Delius",cursive;font-size:20px;line-height:1.3;color:#222;white-space:nowrap}
.contact-line{top:18px;font-size:16px;color:var(--white);letter-spacing:1px;display:flex;align-items:center;gap:10px;white-space:nowrap}
.contact-now{left:990px;top:0;width:166px;height:48px;background:var(--green);border-radius:0 0 12px 12px;color:var(--white);font-family:"Dancing Script",cursive;font-size:26px;display:flex;align-items:center;justify-content:center}
.main-nav{top:78px;left:428px;width:676px;display:flex;justify-content:space-between;font-family:"Arvo",serif;font-size:14px;letter-spacing:1.2px;color:var(--white);white-space:nowrap}
.main-nav .active{position:relative}
.main-nav .active:after{content:"";position:absolute;left:-4px;right:-4px;top:36px;height:5px;background:var(--green)}
.social-dot{left:1122px;top:74px;width:24px;height:24px;border-radius:50%;background:#f6e9c8}
.hero{left:0;top:120px;width:1200px;height:503px;background:linear-gradient(180deg,#3f82d6 0%,#8dbbea 45%,#4f7a34 62%,#cdb99a 80%,#3f7a2a 100%)}
.welcome-box{left:45px;top:533px;width:1111px;height:120px;background:var(--white)}
.down-btn{left:574px;top:508px;width:52px;height:52px;border-radius:50%;background:var(--maroon);display:flex;align-items:center;justify-content:center;z-index:2}
.welcome-title{left:0;top:580px;width:1200px;text-align:center;font-family:"Arvo",serif;font-weight:700;font-size:22px;letter-spacing:2.5px;color:var(--maroon)}
.welcome-text{left:0;top:634px;width:1200px;text-align:center;font-size:16px;line-height:29px;letter-spacing:1.5px;white-space:nowrap}
.card-art{width:210px;height:282px;border-radius:50% 50% 40% 40%/38% 38% 62% 62%;background:linear-gradient(180deg,#7cc9e8 0%,#a9d7ea 40%,#9ccc55 65%,#8b6a3c 100%)}
.card-title{font-family:"Arvo",serif;font-weight:700;font-size:22px;letter-spacing:2.5px;color:var(--maroon);white-space:nowrap}
.card-text{font-size:16px;line-height:27px;letter-spacing:1.3px;white-space:nowrap}
.round-arrow{width:44px;height:44px;border-radius:50%;background:var(--green);display:flex;align-items:center;justify-content:center}
.tents-band{left:51px;top:1144px;width:1102px;height:198px;background:var(--green-band)}
.tent-art{left:105px;top:1165px;width:350px;height:160px;background:linear-gradient(90deg,#2e5a2a,#a0b050 50%,#2e5a2a);border-radius:8px}
.trees-art{left:925px;top:1210px;width:170px;height:92px;background:linear-gradient(180deg,#3c6b35,#1f3f22);border-radius:8px}
.tents-title{left:502px;top:1176px;font-family:"Arvo",serif;font-weight:700;font-size:22px;letter-spacing:2.5px;color:var(--gold)}
.tents-text{left:502px;top:1214px;font-size:16px;line-height:27px;letter-spacing:1.3px;color:#2a2a2a;white-space:nowrap}
.reviews-title{left:0;top:1408px;width:1200px;text-align:center;font-family:"Arvo",serif;font-weight:700;font-size:21px;letter-spacing:2.5px;color:var(--maroon)}
.review-photo{left:44px;top:1483px;width:600px;height:424px;background:linear-gradient(180deg,#3d8fe0 0%,#9cc4ea 30%,#9a9a9a 45%,#8c2c2a 65%,#b8a48a 100%)}
.review-card{left:522px;top:1534px;width:484px;height:325px;background:var(--white);padding:34px 0 0 38px}
.stars{display:flex;gap:12px;margin-bottom:18px}
.review-text{font-size:16px;line-height:27px;letter-spacing:1px;color:#222;white-space:nowrap}
.review-text strong{font-family:"Arvo",serif}
.review-meta{margin-top:18px;margin-left:6px;font-family:"Arvo",serif;font-size:15px;letter-spacing:1.5px;font-weight:700;white-space:nowrap}
.review-meta span{font-weight:400;color:var(--muted);font-size:14px;margin-left:8px}
.read-all{left:664px;top:1876px;font-family:"Arvo",serif;font-weight:700;font-size:16px;letter-spacing:2px;color:var(--green);display:flex;align-items:center;gap:14px;white-space:nowrap}
.cta-band{left:45px;top:1963px;width:1111px;height:179px;background:var(--maroon-dark)}
.fish-art{left:92px;top:2010px;width:140px;height:80px;background:linear-gradient(90deg,#6d8aa0,#3c5568);border-radius:50%}
.cta-text{left:262px;top:2015px;font-family:"Arvo",serif;font-weight:700;font-size:21px;line-height:40px;letter-spacing:2.5px;color:var(--white);white-space:nowrap}
.cta-btn{left:829px;top:2027px;width:258px;height:53px;background:var(--green);border-radius:27px;color:var(--white);font-family:"Arvo",serif;font-weight:700;font-size:21px;letter-spacing:2.5px;display:flex;align-items:center;justify-content:center;gap:18px}
.copyright{left:0;top:2166px;width:1200px;text-align:center;font-size:12px;letter-spacing:1px;color:#444}
</style>
</head>
<body>

<header class="abs site-header"></header>
<div class="abs logo-box">
  <div class="logo-mark"></div>
  <div class="logo-name">Opal's RV Park<br>&amp; Lodge<br>Leeds ND</div>
</div>

<div class="abs contact-line" style="left:342px">
  <svg width="18" height="18" viewBox="0 0 24 24"><path fill="#fff" d="M6.6 10.8a15 15 0 0 0 6.6 6.6l2.2-2.2a1 1 0 0 1 1-.25 11.4 11.4 0 0 0 3.6.6 1 1 0 0 1 1 1V20a1 1 0 0 1-1 1A17 17 0 0 1 3 4a1 1 0 0 1 1-1h3.5a1 1 0 0 1 1 1 11.4 11.4 0 0 0 .6 3.6 1 1 0 0 1-.25 1z"/></svg>
  701-555-0142
</div>
<div class="abs contact-line" style="left:526px">
  <svg width="20" height="18" viewBox="0 0 24 22"><path fill="#fff" d="M2 2h20v14H8l-5 4v-4H2z"/><circle cx="8" cy="9" r="1.5" fill="#7a1a1c"/><circle cx="12" cy="9" r="1.5" fill="#7a1a1c"/><circle cx="16" cy="9" r="1.5" fill="#7a1a1c"/></svg>
  701-555-0187
</div>
<div class="abs contact-line" style="left:702px">
  <svg width="20" height="15" viewBox="0 0 24 18"><rect width="24" height="18" fill="#fff"/><path d="M0 0l12 10L24 0" fill="none" stroke="#7a1a1c" stroke-width="2"/></svg>
  opalsrvlodge@example.com
</div>
<div class="abs contact-now">Contact Now</div>

<nav class="abs main-nav">
  <span class="active">HOME</span><span>LODGING</span><span>RV PARK</span><span>TENTS</span><span>PLACES</span><span>RATES</span><span>FAQ</span><span>REVIEWS</span>
</nav>
<div class="abs social-dot"></div>

<div class="abs hero" role="img" aria-label="Photo of RVs and trailers parked in a row on a gravel lot under a blue sky with trees behind"></div>
<div class="abs welcome-box"></div>
<div class="abs down-btn"><svg width="18" height="12" viewBox="0 0 18 12"><path d="M2 2l7 7 7-7" fill="none" stroke="#fff" stroke-width="3"/></svg></div>

<h1 class="abs welcome-title">WELCOME TO OPAL'S RV PARK &amp; LODGE, LEEDS, NORTH DAKOTA</h1>
<p class="abs welcome-text">Leeds is in the heart of some of the greatest hunting and fishing in the world. Opal's RV Park &amp;<br>Lodge is located right on Highway 2 midway between Devils Lake and Rugby North Dakota. We<br>are smack dab in the middle of it all!</p>

<div class="abs card-art" style="left:64px;top:776px" role="img" aria-label="Illustration of a log cabin on a floating island with trees, clouds and sun"></div>
<h2 class="abs card-title" style="left:326px;top:812px">OPAL'S LODGE</h2>
<p class="abs card-text" style="left:326px;top:870px">Are you looking for a<br>cozy, but spacious home<br>away from home?</p>
<div class="abs round-arrow" style="left:328px;top:994px"><svg width="20" height="14" viewBox="0 0 20 14"><path d="M1 7h17M12 1l6 6-6 6" fill="none" stroke="#fff" stroke-width="2"/></svg></div>

<div class="abs card-art" style="left:632px;top:776px" role="img" aria-label="Illustration of a camper trailer on a floating island with trees, clouds and sun"></div>
<h2 class="abs card-title" style="left:894px;top:812px">OPAL'S RV PARK</h2>
<p class="abs card-text" style="left:894px;top:870px">Opal's RV Park sits right<br>next to Highway 2. Just<br>pull right in and make<br>yourself at home.</p>
<div class="abs round-arrow" style="left:894px;top:994px"><svg width="20" height="14" viewBox="0 0 20 14"><path d="M1 7h17M12 1l6 6-6 6" fill="none" stroke="#fff" stroke-width="2"/></svg></div>

<section class="abs tents-band"></section>
<div class="abs tent-art" role="img" aria-label="Illustration of a green tent among pine trees with a campfire"></div>
<div class="abs trees-art" role="img" aria-label="Illustration of a cluster of pine trees"></div>
<h2 class="abs tents-title">TENTS</h2>
<p class="abs tents-text">Primitive and tent sites, that feature a<br>hot shower, await you.</p>
<svg class="abs" style="left:505px;top:1286px" width="20" height="14" viewBox="0 0 20 14"><path d="M1 7h17M12 1l6 6-6 6" fill="none" stroke="#fff" stroke-width="2"/></svg>

<h2 class="abs reviews-title">FIND OUT WHAT OUR CUSTOMERS ARE SAYING</h2>
<div class="abs review-photo" role="img" aria-label="Photo of the grey and red metal lodge building with a covered porch"></div>
<article class="abs review-card">
  <div class="stars">
    <svg width="26" height="25" viewBox="0 0 24 23"><path fill="#e6cf13" d="M12 0l3.6 7.4 8.1 1.1-5.9 5.7 1.4 8.1L12 18.5l-7.2 3.8 1.4-8.1L.3 8.5l8.1-1.1z"/></svg>
    <svg width="26" height="25" viewBox="0 0 24 23"><path fill="#e6cf13" d="M12 0l3.6 7.4 8.1 1.1-5.9 5.7 1.4 8.1L12 18.5l-7.2 3.8 1.4-8.1L.3 8.5l8.1-1.1z"/></svg>
    <svg width="26" height="25" viewBox="0 0 24 23"><path fill="#e6cf13" d="M12 0l3.6 7.4 8.1 1.1-5.9 5.7 1.4 8.1L12 18.5l-7.2 3.8 1.4-8.1L.3 8.5l8.1-1.1z"/></svg>
    <svg width="26" height="25" viewBox="0 0 24 23"><path fill="#e6cf13" d="M12 0l3.6 7.4 8.1 1.1-5.9 5.7 1.4 8.1L12 18.5l-7.2 3.8 1.4-8.1L.3 8.5l8.1-1.1z"/></svg>
    <svg width="26" height="25" viewBox="0 0 24 23"><path fill="#e6cf13" d="M12 0l3.6 7.4 8.1 1.1-5.9 5.7 1.4 8.1L12 18.5l-7.2 3.8 1.4-8.1L.3 8.5l8.1-1.1z"/></svg>
  </div>
  <p class="review-text"><strong>We love Opal's RV Park &amp; Lodge!</strong> Whenever head<br>out to Devils Lake to Fish this is where we stay.<br>Opal is the sweetest person ever! The facilities<br>are really clean and well cared for. We will be<br>staying at Opal's every time we can come fishing<br>granted there's a spot open for us! Thanks Opal<br>for all you do!</p>
  <p class="review-meta">Dana Holm <span>July 2, 2017 ·</span></p>
</article>
<a class="abs read-all">READ ALL REVIEWS <svg width="22" height="14" viewBox="0 0 22 14"><path d="M1 7h19M14 1l6 6-6 6" fill="none" stroke="#5c8a0a" stroke-width="2"/></svg></a>

<section class="abs cta-band"></section>
<div class="abs fish-art" role="img" aria-label="Illustration of a fish on a fishing line"></div>
<p class="abs cta-text">HEART OF SOME OF THE GREATEST<br>HUNTING AND FISHING IN THE WORLD.</p>
<a class="abs cta-btn">CONTACT <svg width="22" height="14" viewBox="0 0 22 14"><path d="M1 7h19M14 1l6 6-6 6" fill="none" stroke="#fff" stroke-width="2"/></svg></a>

<footer class="abs copyright">(c) Opal's rv park and lodge 2018. All Rights Reserved.</footer>

</body>
</html>
```